New Web-Page Design Required

We need a new or initial web design for our page korvel-net.com. We provide products & services around infrastructure products. We have two products at the moment, but another 2 in the pipeline.
We want to have the following page structure (and part of the project is to design the 7 pages):
- Home
- Products
-One page per product
- Service
- Support
- About
- Contact (Email form)
The start page should include the following information:
- Chirply / Workmesh Links
- Telephone / Email or in general contact details
- News
- Maybe a link-box, where we can highlight/showcase things
- Link to our support portal, quite prominent
- Testimonials
It would be nice if the product pages would have a image header, where we can put up a screenshot or something. Links to datasheet and videos of the product would be nice as well.
We like the "big banner in the middle" designs, like these two Vendra examples. No need to copy them, it should just give you an idea.
http://www.plomdesigns.com/itempreview/185
http://www.plomdesigns.com/content/pdk42/index.php
Budget for images available, so please use placeholders or ask us for specific photos/images, if you need them for your design.
Target Market(s)
Business-2-Business, Decision makers and Technical Leads
Industry/Entity Type
News
Look and feel
Each slider illustrates characteristics of the customer's brand and the style your logo design should communicate.

```html
<!DOCTYPE html>
<html lang="en">
<head>
<meta charset="utf-8">
<title>Korvel Net — Home</title>
<link href="https://fonts.googleapis.com/css2?family=Roboto:wght@400;500;700&family=Roboto+Condensed:wght@700&family=Open+Sans:wght@300;400;600&family=Bitter:wght@300;400&display=swap" rel="stylesheet">
<style>
:root{
  --teal:#13a3b3;
  --teal-dark:#1b8a8f;
  --blue:#1e5d94;
  --ink:#333;
  --muted:#9a9a9a;
  --nav-top:#444;
  --nav-bottom:#1f1f1f;
  --quote:#2fb3c5;
  --footer:#2b2b2b;
  --footer-base:#1f1f1f;
  --footer-link:#a9a9a9;
}
*{margin:0;padding:0;box-sizing:border-box}
html,body{width:926px;height:1200px;overflow:hidden}
body{position:relative;background:#fbfbfb;font-family:"Open Sans",sans-serif;color:var(--ink)}
.abs{position:absolute}
a{color:inherit;text-decoration:none}

.brand{left:98px;top:34px}
.brand-name{font-family:"Roboto",sans-serif;font-weight:500;font-size:28px;color:#3d3d3d;letter-spacing:-0.3px}
.social{right:97px;top:13px;display:flex;gap:6px;font-family:"Roboto",sans-serif;font-size:9px;font-weight:500}
.social a{background:var(--teal);color:#fff;padding:5px 5px;border-radius:2px}
.contact{right:97px;top:44px;text-align:right;display:flex;align-items:center;gap:8px}
.contact-lines small{display:block;font-size:10px;color:#37476a}
.contact-lines strong{display:block;font-family:"Roboto",sans-serif;font-weight:400;font-size:18px;color:#222;letter-spacing:.5px;line-height:20px}

.nav{left:85px;top:91px;width:756px;height:38px;background:linear-gradient(var(--nav-top),var(--nav-bottom));border-bottom:4px solid var(--teal)}
.nav a{position:absolute;top:0;height:34px;line-height:34px;font-family:"Roboto Condensed",sans-serif;font-weight:700;font-size:13px;color:#fff;transform:translateX(-50%);padding:0 15px}
.nav a.active{background:var(--teal-dark);top:6px;height:25px;line-height:25px}

.hero{left:85px;top:134px;width:756px;height:312px;background:linear-gradient(100deg,#6f8aa0 0%,#9fb3c4 25%,#5c6673 50%,#2f353d 75%,#22272e 100%)}
.hero-base{left:85px;top:446px;width:756px;height:5px;background:var(--teal)}
.headline{left:105px;top:356px;font-weight:300;font-size:27px;letter-spacing:-1.3px;color:#fff}
.headline-box{left:85px;top:392px;width:312px;height:39px;background:rgba(235,235,235,.72);padding-left:20px;font-weight:400;font-size:27px;line-height:39px;letter-spacing:-1.3px;color:#454545}
.portal{left:401px;top:429px;width:124px;height:36px;border-radius:18px;background:linear-gradient(#1cb7c7,#0e97a6);box-shadow:0 2px 3px rgba(0,0,0,.25);color:#fff;font-family:"Roboto",sans-serif;font-weight:500;font-size:11.5px;text-align:center;line-height:36px}
.dots{left:770px;top:464px;display:flex;gap:8px}
.dots span{width:7px;height:7px;border-radius:50%;background:#a7a7a7}
.dots span.on{background:var(--blue)}

.welcome{left:98px;top:480px;width:490px}
.welcome h1{font-family:"Roboto",sans-serif;font-weight:400;font-size:21px;color:var(--blue);height:39px}
.rule{height:1px;background:#cfcfcf;position:relative;margin-bottom:12px}
.rule::after{content:"";position:absolute;left:14px;top:-3px;width:6px;height:6px;background:#fbfbfb;border-right:1px solid #cfcfcf;border-bottom:1px solid #cfcfcf;transform:rotate(45deg)}
.welcome p{font-size:9.6px;line-height:17px;color:var(--muted);margin-bottom:14px}
.news{left:618px;top:488px;width:211px}
.news h2{font-family:"Roboto",sans-serif;font-weight:400;font-size:15px;color:#333;height:31px}
.news p{font-size:9.3px;line-height:15.5px;color:var(--muted);letter-spacing:.2px}
.news .meta{display:flex;justify-content:space-between;padding:0 12px 0 0;font-size:8.5px;color:#333;margin:2px 0 9px}
.news .meta em{font-style:normal;color:var(--quote)}

.portfolio{left:0;top:653px;width:926px;height:183px;background:linear-gradient(#ececec,#f1f1f1)}
.portfolio h2{position:absolute;left:96px;top:20px;font-family:"Roboto",sans-serif;font-weight:400;font-size:17px;color:#333}
.case{position:absolute;top:52px;width:161px;text-align:center}
.case .shot{height:82px;background:#fff;border:1px solid #ddd;padding:4px}
.case .shot div{height:100%;background:linear-gradient(#2b2f33,#181b1e)}
.case span{display:block;margin-top:10px;font-family:"Roboto",sans-serif;font-size:12.5px;color:#222}
.case-sep{position:absolute;top:55px;width:0;height:76px;border-left:1px dashed #d2d2d2}

.clients{left:0;top:836px;width:926px;height:167px;background:#f8f8f8;text-align:center}
.clients h2{margin-top:21px;font-family:"Bitter",serif;font-weight:300;font-size:25px;color:#444}
.clients h2 b{font-family:"Bitter",serif;font-weight:400;font-size:54px;color:#c6c6c6;vertical-align:-22px;line-height:0;margin:0 8px}
.clients blockquote{margin-top:12px;font-size:12.2px;line-height:17px;color:var(--quote)}
.clients .who{margin-top:8px;font-size:12.5px;font-weight:600;color:#333}
.clients .where{font-size:9px;color:#888}

.footer{left:0;top:1003px;width:926px;height:165px;background:var(--footer);border-top:3px solid #bdbdbd}
.col{position:absolute;top:22px}
.col h3{font-weight:400;font-size:17px;color:#fff;margin-bottom:10px}
.col li{list-style:none;font-size:10px;line-height:15.5px;color:var(--footer-link);letter-spacing:1px}
.col .gap{height:7px}
.map{position:absolute;left:607px;top:52px;width:214px;height:97px;border:2px solid #cfcfcf;background:linear-gradient(135deg,#e6e0c8,#d9d4bf 60%,#c9d7b8)}
.base{left:0;top:1168px;width:926px;height:32px;background:var(--footer-base);font-size:10px;color:#eee;letter-spacing:.3px}
.base .copy{position:absolute;left:105px;top:9px}
.base .legal{position:absolute;right:107px;top:9px}
</style>
</head>
<body>

<div class="abs brand"><span class="brand-name">Korvel Net</span></div>
<nav class="abs social"><a href="#">Chirply</a><a href="#">Workmesh</a></nav>
<div class="abs contact">
  <svg width="28" height="30" viewBox="0 0 28 30" aria-hidden="true"><path d="M4 16a10 10 0 0 1 20 0" fill="none" stroke="#333" stroke-width="2.4"/><rect x="2" y="14" width="6" height="10" rx="2" fill="#333"/><rect x="20" y="14" width="6" height="10" rx="2" fill="#333"/><path d="M23 24c0 3-4 4-8 4" fill="none" stroke="#333" stroke-width="1.6"/></svg>
  <div class="contact-lines"><small>Contact us for a free estimate</small><strong>1-800-555-0142</strong></div>
</div>

<nav class="abs nav">
  <a class="active" href="#" style="left:79px">Home</a>
  <a href="#" style="left:187px">Products</a>
  <a href="#" style="left:316px">Service</a>
  <a href="#" style="left:443px">Support</a>
  <a href="#" style="left:565px">About</a>
  <a href="#" style="left:687px">Contact</a>
</nav>

<div class="abs hero" role="img" aria-label="Photo of a person holding a tablet beneath a cloud with connected device icons, server racks blurred behind"></div>
<div class="abs hero-base"></div>
<div class="abs headline">We Commit To What</div>
<div class="abs headline-box">Others Walk Away From</div>
<a class="abs portal" href="#">SUPPORT PORTAL</a>
<div class="abs dots"><span></span><span></span><span class="on"></span><span></span></div>

<section class="abs welcome">
  <h1>Welcome to Korvel Net</h1>
  <div class="rule"></div>
  <p>Lorem Ipsum est simplement du faux texte employé dans la sition et la misen page avant impression. Le Lorem Ipsum est le faux texte standard de l'imprimerie depuis les années 1500,réaliser un livre spécimen de polices de texte. Il a été popularisé dans les années 1960.</p>
  <p>Grâce à la vente de feuilles Printwell contenant des passages du Lorem Ipsum, et, plus récemment, par son inclusion dans des applications de mise en page de texte, comme Layoutly Studio.</p>
</section>

<section class="abs news">
  <h2>NEW &amp; EVENTS</h2>
  <div class="rule"></div>
  <p>Lorem Ipsum est mplement du faux texte liser un livre composition.</p>
  <div class="meta"><em>"Anonymous"</em><span>08-June-2013</span></div>
  <p>Lorem Ipsum est mplement du faux texte liser un livre composition.</p>
  <div class="meta"><em>"Anonymous"</em><span>08-June-2013</span></div>
</section>

<section class="abs portfolio">
  <h2>Our Portfolio</h2>
  <div class="case" style="left:96px"><div class="shot"><div role="img" aria-label="Screenshot of a network monitoring dashboard"></div></div><span>Case&nbsp; 01</span></div>
  <div class="case-sep" style="left:272px"></div>
  <div class="case" style="left:288px"><div class="shot"><div role="img" aria-label="Screenshot of a distribution chart dashboard"></div></div><span>Case 02</span></div>
  <div class="case-sep" style="left:463px"></div>
  <div class="case" style="left:478px"><div class="shot"><div role="img" aria-label="Screenshot of a network monitoring dashboard"></div></div><span>Case 03</span></div>
  <div class="case-sep" style="left:654px"></div>
  <div class="case" style="left:670px"><div class="shot"><div role="img" aria-label="Screenshot of a bandwidth graph dashboard"></div></div><span>Case 04</span></div>
</section>

<section class="abs clients">
  <h2><b>“</b>Happy Clients<b>”</b></h2>
  <blockquote>“Lorem Ipsum est simplement du faux texte employé dans la sition et la est faux misen page avant impression.<br>Le Lorem Ipsum est le faux texte standard de l'imprimerie depuis les années anonyme 1500”</blockquote>
  <div class="who">Dorian Feltham</div>
  <div class="where">Halden, Norway</div>
</section>

<footer class="abs footer">
  <div class="col" style="left:117px"><h3>SiteMap</h3><ul><li>Our Associates</li><li>Our Location</li><li>Our Services</li><li>Our Qualifications</li><li>Our Articles</li><li>External Page</li></ul></div>
  <div class="col" style="left:261px"><h3>Quick Links</h3><ul><li>Our Associates</li><li>Our Location</li><li>Our Services</li><li>Our Qualifications</li><li>Our Articles</li><li>External Page</li></ul></div>
  <div class="col" style="left:411px"><h3>Contact Details</h3><ul><li>PO Box 418, MERIDALE QLD 4999</li><li class="gap"></li><li>Phone: 1 300 555 019</li><li>Fax: 1 300 555 019</li><li class="gap"></li><li>hello@korvel-net.com</li><li>Map and Directions</li></ul></div>
  <div class="col" style="left:606px"><h3>Our Location</h3></div>
  <div class="map" role="img" aria-label="Street map of the office location"></div>
</footer>
<div class="abs base"><span class="copy">Copyright 2012 Website Name. All Rights Reserved.</span><span class="legal">Privacy Policy | Terms &amp; Condition</span></div>

</body>
</html>
```